Brightford Lingua Partners, LLC

We need a business card that includes information about our business and conveys a reliable business that provides document translation services and interpreters for a variety of corporate and individual clients. We want to come across as professional, reliable, yet approachable. It should include the following on one side:

ESL / ENL Language Classes, Private Lessons, and Online Tutors
PALQE Training and Testing
Translating & Interpreting Services
Contact us about Over-the-Phone Interpreting in over 200 languages
24/7/365
www.brightfordlingua.example

The other side should include (555) 481-3062

Marla Quennick, President
412 Garvin Ave., Ste. 209
Indianapolis, IN 46999
Updates

Please add USA as part of the address. Also, please add mrqquennick@brightfordlinguapartners.example as the e-mail address. Thank you.

Target Market(s)

Business professionals, their families, the international community

Industry/Entity Type

Business

Contact Information for Business Card

24/7/365
www.brightfordlingua.example

(555) 481-3062

Marla Quennick, President
412 Garvin Ave., Ste. 209
Indianapolis, IN 46999
USA

Font styles to use
Sans Serif

Colors

Designer to choose colors to be used in the design.

Requirements
Must have
• See project description
• e-mail address and web address
• Phone number
Nice to have
• a globe
• physical address
Should not have
• Should not have the same color scheme as other agencies in our market in Indiana unless it is blue and black. No purple or yellow.

```html
<!DOCTYPE html>
<html lang="en">
<head>
<meta charset="utf-8">
<title>Brightford Lingua Partners — Business Card</title>
<link href="https://fonts.googleapis.com/css2?family=Cabin:wght@400;500;600;700&display=swap" rel="stylesheet">
<style>
  :root {
    --brand-blue: #2a8fd0;
    --brand-green: #9cc23c;
    --ink: #141414;
    --muted: #8c8c8c;
    --paper: #ffffff;
    --backdrop: #d3d3d3;
  }
  * { box-sizing: border-box; margin: 0; padding: 0; }
  html, body {
    width: 1200px; height: 1064px; overflow: hidden;
    background: var(--backdrop);
    font-family: "Cabin", "Gill Sans", sans-serif;
  }
  .sheet {
    position: relative; width: 1200px; height: 1064px;
    display: flex; flex-direction: column; align-items: center;
    justify-content: center; gap: 40px;
  }
  .card {
    position: relative; width: 840px; height: 480px; overflow: hidden;
    box-shadow: 0 6px 18px rgba(0,0,0,.18);
  }
  .card-art { position: absolute; inset: 0; width: 100%; height: 100%; }

  /* Front */
  .card-front { background: var(--paper); color: var(--ink); }
  .brand-lockup {
    position: absolute; left: 330px; top: 48px;
    display: flex; align-items: center; gap: 16px;
  }
  .brand-dot {
    width: 96px; height: 96px; border-radius: 50%;
    background: var(--brand-blue); flex: none;
  }
  .brand-name {
    font-size: 36px; line-height: 1.02; font-weight: 500; color: var(--ink);
  }
  .contact-person { position: absolute; left: 200px; top: 238px; }
  .person-name { font-size: 27px; font-weight: 500; letter-spacing: .5px; }
  .person-title { font-size: 21px; font-weight: 700; color: var(--muted); margin-top: -2px; }
  .postal-address {
    font-style: normal; font-size: 21px; line-height: 1.28; margin-top: 18px;
  }

  /* Back */
  .card-back { background: var(--brand-blue); color: #fff; }
  .brand-lockup-small {
    position: absolute; left: 40px; top: 132px;
    display: flex; align-items: center; gap: 10px;
  }
  .brand-lockup-small .brand-dot { width: 54px; height: 54px; background: #fff; }
  .brand-lockup-small .brand-name { font-size: 18px; color: #fff; line-height: 1.05; }
  .service-list {
    position: absolute; left: 40px; top: 212px; width: 400px;
    list-style: none; font-size: 21px; line-height: 1.2;
  }
  .service-list li { position: relative; padding-left: 22px; margin-bottom: 3px; white-space: nowrap; }
  .service-list li::before {
    content: ""; position: absolute; left: 0; top: 8px;
    width: 10px; height: 10px; border-radius: 50%; background: var(--brand-green);
  }
  .availability-band {
    position: absolute; left: 0; top: 396px; width: 250px; height: 62px;
    background: var(--brand-green); display: flex; align-items: center;
    padding-left: 40px; font-size: 40px; font-weight: 700; letter-spacing: 1px;
  }
  .contact-lines {
    position: absolute; right: 36px; top: 300px; text-align: right;
  }
  .contact-phone { font-size: 38px; font-weight: 400; letter-spacing: 1px; }
  .contact-email { font-size: 17px; margin-top: 4px; }
  .contact-web { font-size: 24px; font-weight: 700; margin-top: 4px; }
</style>
</head>
<body>
<main class="sheet">

  <section class="card card-front" aria-label="Business card front">
    <svg class="card-art" viewBox="0 0 840 480">
      <defs>
        <radialGradient id="globe-tone" cx="45%" cy="40%" r="65%">
          <stop offset="0%" stop-color="#9cc23c"/>
          <stop offset="55%" stop-color="#5ea98a"/>
          <stop offset="100%" stop-color="#2a8fd0"/>
        </radialGradient>
      </defs>
      <circle cx="-110" cy="400" r="290" fill="#2a8fd0"/>
      <circle cx="-110" cy="400" r="264" fill="#fff"/>
      <circle cx="-110" cy="400" r="254" fill="#2a8fd0"/>
      <circle cx="-110" cy="400" r="244" fill="#fff"/>
      <circle cx="-110" cy="400" r="238" fill="#2a8fd0"/>
      <g role="img" aria-label="Illustrated globe showing green continents on blue oceans">
        <circle cx="790" cy="470" r="230" fill="url(#globe-tone)"/>
      </g>
    </svg>

    <div class="brand-lockup">
      <span class="brand-dot" aria-hidden="true"></span>
      <p class="brand-name">Brightford<br>Lingua Partners<br>LLC</p>
    </div>

    <div class="contact-person">
      <p class="person-name">MARLA QUENNICK</p>
      <p class="person-title">President</p>
      <address class="postal-address">
        412 Garvin Ave., Ste. 209<br>
        Indianapolis, IN 46999<br>
        USA
      </address>
    </div>
  </section>

  <section class="card card-back" aria-label="Business card back">
    <svg class="card-art" viewBox="0 0 840 480">
      <defs>
        <radialGradient id="globe-tone-back" cx="50%" cy="70%" r="70%">
          <stop offset="0%" stop-color="#2a8fd0"/>
          <stop offset="60%" stop-color="#5ea98a"/>
          <stop offset="100%" stop-color="#9cc23c"/>
        </radialGradient>
      </defs>
      <circle cx="600" cy="10" r="222" fill="none" stroke="#fff" stroke-width="3"/>
      <g role="img" aria-label="Illustrated globe showing green continents on blue oceans">
        <circle cx="600" cy="10" r="218" fill="url(#globe-tone-back)"/>
      </g>
    </svg>

    <div class="brand-lockup-small">
      <span class="brand-dot" aria-hidden="true"></span>
      <p class="brand-name">Brightford<br>Lingua Partners<br>LLC</p>
    </div>

    <ul class="service-list">
      <li>ESL / ENL Language Classes,<br>Private Lessons, and Online Tutors</li>
      <li>PALQE Training and Testing</li>
      <li>Translating &amp; Interpreting Services</li>
      <li>Contact us about Over-the-Phone<br>Interpreting in over 200 languages</li>
    </ul>

    <div class="availability-band">24·7·365</div>

    <div class="contact-lines">
      <p class="contact-phone">(555) 481-3062</p>
      <p class="contact-email">mrqquennick@brightfordlinguapartners.example</p>
      <p class="contact-web">www.brightfordlingua.example</p>
    </div>
  </section>

</main>
</body>
</html>
```